7th Annual Falcon Ridge Classic Flyer

Looking to design an updated eye catching flyer maybe with someone movement, sound, and color. Below is an attachment of the flyer I have used in the past. I need to add color, sound, and movement to the flyer. This is an advertisement for youth folk style wrestling. You may contact me directly at 252-381-4927 if you need additional information. I really like the colors music and movement in the video below.
https://www.vidloomer.com/watch?v=kQ7mTbLw2Ra

Target Market(s)

Youth Wrestling

Font styles to use
Serif

Colors
EB3D1F
EC4F4E
F09395
F8D3D4
FCEDEE

Requirements
Must have
• All information included on flyer.
Nice to have
• Color, sound, and movement

```html
<!DOCTYPE html>
<html lang="en">
<head>
<meta charset="utf-8">
<title>7th Annual Falcon Ridge Classic</title>
<link href="https://fonts.googleapis.com/css2?family=Cinzel:wght@400;700;900&family=Playfair+Display:wght@700;900&family=Marcellus&family=Oswald:wght@400;500;600&family=Poppins:wght@400;500;600;700&display=swap" rel="stylesheet">
<style>
:root{
  --stage:#2b2b2b;
  --brown-deep:#3a2216;
  --brown-mid:#7a4a2c;
  --tan-light:#d9b48a;
  --cream:#f4ecdf;
  --band:#3b2419;
  --orange:#c9621b;
  --gold-1:#f6d680;
  --gold-2:#e7b21c;
  --gold-3:#c99a3a;
  --ink:#2a1c14;
  --white:#ffffff;
}
*{margin:0;padding:0;box-sizing:border-box}
html,body{width:1200px;height:1200px;overflow:hidden;background:var(--stage)}
.flyer{position:absolute;left:190px;top:20px;width:820px;height:1160px;overflow:hidden;color:var(--ink)}
.flyer-backdrop{position:absolute;inset:0;
  background:radial-gradient(ellipse 75% 58% at 55% 48%,#e2c29a 0%,#b9855a 38%,#7b4a2c 68%,var(--brown-deep) 100%)}
.warrior-art{position:absolute;left:150px;top:0;width:290px;height:400px;
  background:radial-gradient(ellipse 62% 62% at 50% 38%,rgba(104,88,70,.85) 0%,rgba(110,58,36,.7) 38%,rgba(122,74,44,.35) 62%,rgba(122,74,44,0) 82%)}
.date-box{position:absolute;left:61px;top:42px;width:119px;height:256px;border:1.5px solid var(--white);
  font-family:'Oswald',sans-serif;color:var(--white);text-align:center;line-height:.9}
.date-day{font-size:37px;font-weight:500;letter-spacing:-1px;margin-top:12px;transform:scaleX(.78)}
.date-month{font-size:104px;font-weight:500;letter-spacing:-4px;transform:scaleX(.8);margin-top:-2px}
.date-num{font-size:96px;font-weight:500;letter-spacing:-4px;transform:scaleX(.8)}
.date-num sup{font-size:50px;vertical-align:top;position:relative;top:4px}
.title{position:absolute;left:393px;top:80px;width:400px}
.title-ordinal{font-family:'Playfair Display',serif;font-weight:900;color:var(--white);line-height:1;font-size:150px;height:150px}
.title-ordinal sup{font-size:76px;vertical-align:top;position:relative;top:14px;font-weight:700}
.gold{background:linear-gradient(180deg,var(--gold-1),var(--gold-2) 60%,var(--gold-3));-webkit-background-clip:text;background-clip:text;color:transparent}
.title-annual{position:absolute;left:54px;top:88px;font-family:'Cinzel',serif;font-weight:700;font-size:62px;line-height:1}
.title-name{position:absolute;left:4px;top:160px;font-family:'Cinzel',serif;font-weight:900;font-size:40px;line-height:1;white-space:nowrap;letter-spacing:-.5px}
.title-sub{position:absolute;left:6px;top:212px;font-family:'Cinzel',serif;font-weight:700;font-size:44px;line-height:1;color:var(--gold-3)}
.league{position:absolute;left:618px;top:30px;width:176px;text-align:center}
.league-mark{display:flex;align-items:center;justify-content:center;gap:8px;height:70px}
.league-dot{width:26px;height:26px;border-radius:50%;background:var(--cream)}
.league-name{font-family:'Cinzel',serif;font-weight:900;font-size:28px;color:var(--cream)}
.league-tag{font-family:'Cinzel',serif;font-weight:700;font-size:9.5px;color:var(--cream);line-height:1.35;margin-top:4px}
.venue{position:absolute;left:97px;top:351px;width:621px;height:75px}
.venue-scroll{position:absolute;inset:6px 20px;border-radius:6px;
  background:linear-gradient(180deg,#f2dca5,#e3c07c 60%,#d6ab62)}
.venue-text{position:absolute;inset:0;display:flex;flex-direction:column;justify-content:center;align-items:center;
  font-family:'Poppins',sans-serif;font-weight:600;font-size:20px;line-height:1.12;color:#3a2a1c}
.start-times{position:absolute;left:0;width:820px;top:431px;text-align:center;font-family:'Marcellus',serif;font-size:19px;line-height:23px;color:var(--ink)}
.register{position:absolute;left:36px;top:485px;width:753px;height:140px;border:1.5px solid var(--ink);border-radius:3px;
  font-family:'Oswald',sans-serif;text-align:center;font-size:20.5px;line-height:24.2px;padding-top:6px;letter-spacing:.4px}
.register b{font-weight:600}
.card-note{position:absolute;left:0;width:820px;top:630px;text-align:center;font-family:'Poppins',sans-serif;font-weight:700;font-size:14px;color:#3a2416;letter-spacing:.3px}
.divisions{position:absolute;left:36px;top:658px;width:753px;height:240px;background:var(--cream)}
.divisions-head{display:flex;height:39px;background:var(--band);color:var(--white);font-family:'Marcellus',serif;font-size:22px}
.divisions-head span{flex:1;text-align:center;line-height:40px}
.divisions-body{display:flex;font-family:'Poppins',sans-serif;font-size:11.6px;line-height:15.2px;color:#222}
.col-boys{width:388px;padding:10px 10px 0 21px}
.col-girls{flex:1;padding:8px 18px 0 14px;line-height:19.5px}
.divisions-body b{font-weight:700}
.age-note{margin-top:18px;font-weight:700;font-size:18px;line-height:20px;text-align:center;color:#2c1d14}
.director-note{position:absolute;left:36px;top:907px;width:753px;height:33px;background:var(--orange);color:var(--white);
  font-family:'Marcellus',serif;font-size:17px;text-align:center;line-height:33px;letter-spacing:.3px}
.details{position:absolute;left:36px;top:940px;width:753px;height:124px;background:rgba(58,34,22,.78);display:flex;color:var(--white)}
.rules{width:370px;padding:8px 12px 0 14px;font-family:'Poppins',sans-serif;font-size:10.2px;line-height:13.4px;text-align:justify;letter-spacing:.6px}
.weighins{flex:1;padding:6px 8px 0 18px;font-family:'Oswald',sans-serif;font-size:13.6px;line-height:18px}
.weighins h3{font-weight:600;color:var(--gold-2);font-size:20px;line-height:22px}
.contact-bar{position:absolute;left:36px;top:1068px;width:753px;height:32px;display:flex;font-family:'Oswald',sans-serif;font-size:14px;color:var(--white);letter-spacing:.5px}
.contact-bar .admission{width:367px;background:var(--band);line-height:32px;padding-left:13px}
.contact-bar .director{flex:1;background:var(--orange);line-height:32px;padding-left:6px}
.hotels{position:absolute;left:36px;width:753px;top:1108px;font-family:'Poppins',sans-serif;font-size:13px;color:var(--white);white-space:nowrap}
.hotels b{font-weight:700}
</style>
</head>
<body>
<main class="flyer">
  <div class="flyer-backdrop" role="img" aria-label="Warm dusty battlefield background in brown and tan tones"></div>
  <div class="warrior-art" role="img" aria-label="Illustration of a helmeted ancient warrior with a red cape"></div>

  <div class="date-box">
    <div class="date-day">SATURDAY</div>
    <div class="date-month">JAN</div>
    <div class="date-num">25<sup>TH</sup></div>
  </div>

  <div class="league">
    <div class="league-mark"><span class="league-dot"></span><span class="league-name">CYML</span></div>
    <div class="league-tag">CAROLINA'S PREMIER<br>YOUTH MAT LEAGUE</div>
  </div>

  <h1 class="title">
    <div class="title-ordinal">7<sup>th</sup></div>
    <div class="title-annual gold">ANNUAL</div>
    <div class="title-name gold">FALCON RIDGE</div>
    <div class="title-sub">CLASSIC</div>
  </h1>

  <div class="venue">
    <div class="venue-scroll" role="img" aria-label="Parchment scroll banner"></div>
    <div class="venue-text"><span>Pinecrest Event Center 415</span><span>Harbor Blvd SW Pinecrest, NC 27590</span></div>
  </div>

  <div class="start-times">
    4U, 6U, 8U, 10U – WRESTLING STARTS AT 8:30 AM<br>
    12U, MIDDLE SCHOOL, &amp; HIGH SCHOOL – WRESTLING STARTS AT 1:00 PM
  </div>

  <div class="register">
    REGISTER @ WWW.MATBRACKET.COM<br>
    EARLY REGISTRATION $30.00 <b>DEADLINE IS JANUARY 19, 2025 AT 11:59PM</b><br>
    REGULAR REGISTRATION $40.00 <b>DEADLINE IS JANUARY 22, 2025 AT 11:59PM</b><br>
    LATE REGISTRATION $50.00 <b>DEADLINE IS JANUARY 24, 2025 AT 5:00PM</b><br>
    REGISTRATION IS LIMITED TO THE FIRST 500 WRESTLERS
  </div>

  <p class="card-note">NON-CYML CARD HOLDERS WILL PAY AN ADDITIONAL $5.00 AT WEIGH-INS.</p>

  <section class="divisions">
    <div class="divisions-head"><span>BOYS DIVISIONS</span><span>GIRLS DIVISIONS</span></div>
    <div class="divisions-body">
      <div class="col-boys">
        <b>4 &amp; UNDER</b> - 30, 40, 50, HWT<br>
        <b>6 &amp; UNDER</b> - 36, 40, 44, 48, 52, 56, 60, HWT<br>
        <b>8 &amp; UNDER</b> - 40, 44, 48, 52, 56, 60, 64, 68, 72, 76, 80, 84, 88, 92, HWT<br>
        <b>10 &amp; UNDER</b> - 52, 56, 60, 64, 68, 72, 76, 80, 84, 88, 92, 96, 100, 110, HWT<br>
        <b>12 &amp; UNDER</b> - 64, 68, 72, 76, 80, 84, 88, 92, 96, 100, 105, 110, 115, 120, 130, 140, 160, HWT<br>
        <b>MIDDLE SCHOOL</b> - 72, 76, 80, 88, 92, 96, 100, 105, 110, 115, 120, 130, 140, 160, 210, HWT<br>
        <b>HIGH SCHOOL</b> - 106, 113, 120, 126, 132, 138, 144, 150, 157, 165, 175, 190, 215, HWT
      </div>
      <div class="col-girls">
        <b>K-5</b> - 36, 40, 44, 48, 52, 56, 60, 64, 68, 72, 76, 80, 84, 88, 92, 96, 100, 110, 120,HWT<br>
        <b>MIDDLE SCHOOL</b> – 72, 76, 83, 90, 98, 106, 113, 120, 126, 132, 138, 145, 152, 160, 170, 182, 190, 220, HWT<br>
        <b>WOMEN'S HIGH SCHOOL</b> 100, 107, 114, 120, 126, 132, 145, 152, 165, 185, HWT
        <p class="age-note">*AGE IS BASED UPON WRESTLER'S AGE AS OF DECEMBER 31, 2024.</p>
      </div>
    </div>
  </section>

  <p class="director-note">Tournament director has the right to combine weight classes if deemed necessary.</p>

  <section class="details">
    <p class="rules">Tenths are waived/dropped at weigh-ins. Satellite weigh-ins will not be allowed. High School Divisions are given 2 lbs. growth allowance. Custom medals will be given to the top 3 individual finishers in each bracket. Custom Awards will be awarded to the top 4 teams. Referee decisions will be final. Cedar Creek Athletics is not responsible for accidents, injuries, or theft during the tournament.</p>
    <div class="weighins">
      <h3>WEIGH-INS:</h3>
      JANUARY 24, 2025 - 5:00 PM TO 7:00 PM (EARLY WEIGH-INS - $10 CASH DUE AT SCALE)<br>
      JANUARY 25, 2025 - 6:00 AM TO 7:30 AM (4U, 6U, 8U, 10U)<br>
      JANUARY 25, 2025 - 11:00 AM TO 12:00 PM (12 &amp; UNDER, MS, &amp; HIGH SCHOOL)
    </div>
  </section>

  <div class="contact-bar">
    <span class="admission">ADMISSION: $10.00 PER PERSON FOR MORE INFORMATION,</span>
    <span class="director">CONTACT TOURNAMENT DIRECTOR DALE PORTER: (252) 381-4927</span>
  </div>

  <p class="hotels"><b>Hotels Available On-Site</b> Lakeview Hotel (252) 410-2200 / Maple Suites (252) 410-3300 / Harbor Lodge (252) 410-4400</p>
</main>
</body>
</html>
```